Redesign of Business Card to look more professional and stand out

Business card design. You can lean more about our company by going to dlmfabworks.example. Raised letters would be nice. Company name & Address
DL&M
418 Wrenfield Crest Drive, Suite 140
Birmingham, AL 35999

You can use my name and title: Glenn Marlowe
Business Development Manager

Target Market(s)

Heavy Industrial market, i.e. utilities, chemical plants, paper mills, construction companies

Industry/Entity Type

Construction

Contact Information for Business Card

We provide Project Management & Project Support Services

Font styles to use
Serif

Requirements
Must have
• Company name & Address
• DL&M
• 418 Wrenfield Crest Drive, Suite 140
• Birmingham, AL 35999
Nice to have
• ideas for the back of the card
Should not have
• no crazy colors. needs to look professional and standout.

```html
<!DOCTYPE html>
<html lang="en">
<head>
<meta charset="utf-8">
<title>DL&amp;M Business Card</title>
<link rel="stylesheet" href="https://fonts.googleapis.com/css2?family=Tinos:wght@400;700&display=swap">
<style>
  :root {
    --navy: #1d3866;
    --navy-line: #2451a3;
    --ink: #1a1a1a;
    --paper: #ffffff;
    --backdrop: #e4e6e9;
    --steel-light: #dfeaf5;
    --steel-mid: #7fa6c9;
    --steel-dark: #1f3f66;
  }
  * { box-sizing: border-box; margin: 0; padding: 0; }
  html, body {
    width: 1189px; height: 1200px; overflow: hidden;
    background: var(--backdrop);
    font-family: "Tinos", "Times New Roman", serif;
  }
  .card {
    position: absolute; left: 137px; width: 916px; height: 524px;
    background: var(--paper);
    box-shadow: 0 4px 12px rgba(0,0,0,0.25);
    overflow: hidden;
  }
  .card-front { top: 45px; }
  .card-back { top: 600px; }

  .wordmark {
    position: absolute; left: 0; right: 0; text-align: center;
    color: var(--navy); font-weight: 700; letter-spacing: 2px; line-height: 1;
  }
  .card-front .wordmark { top: 28px; font-size: 228px; }

  .identity {
    position: absolute; left: 30px; width: 360px; top: 310px; text-align: center;
  }
  .identity .name { color: var(--navy); font-size: 42px; line-height: 1; }
  .identity .title { color: var(--ink); font-size: 24px; margin-top: 8px; }

  .divider {
    position: absolute; left: 404px; top: 257px; width: 2px; height: 162px;
    background: var(--ink);
  }

  .contact { position: absolute; left: 440px; top: 265px; list-style: none; }
  .contact li {
    display: flex; align-items: flex-start; gap: 12px;
    font-size: 26px; color: var(--ink); line-height: 32px; margin-bottom: 9px;
  }
  .contact li:last-child { margin-top: -4px; }
  .contact .icon { width: 18px; height: 18px; flex: none; margin-top: 7px; }

  .rule { position: absolute; left: 0; right: 0; top: 470px; height: 3px; background: var(--navy-line); }
  .band { position: absolute; left: 0; right: 0; top: 473px; bottom: 0; background: var(--navy); }

  .plant-photo {
    position: absolute; inset: 0;
    background: linear-gradient(180deg, var(--steel-mid) 0%, var(--steel-light) 40%, var(--steel-mid) 70%, var(--steel-dark) 100%);
  }
  .logo-strip {
    position: absolute; left: 0; right: 0; top: 185px; height: 162px;
    background: rgba(255,255,255,0.6);
  }
  .card-back .wordmark { top: 200px; font-size: 150px; }
</style>
</head>
<body>
  <section class="card card-front">
    <div class="wordmark">DL&amp;M</div>

    <div class="identity">
      <p class="name">Glenn Marlowe</p>
      <p class="title">Business Development Manager</p>
    </div>

    <div class="divider"></div>

    <ul class="contact">
      <li>
        <svg class="icon" viewBox="0 0 18 18"><rect width="18" height="18" fill="#1d3866"/><path d="M5 4l2.5 0 1 3-1.5 1c.7 1.5 1.5 2.3 3 3l1-1.5 3 1V14c-5 .5-9.5-4-9-10z" fill="#fff"/></svg>
        <span>205-555-0142</span>
      </li>
      <li>
        <svg class="icon" viewBox="0 0 18 18"><rect width="18" height="18" fill="#1d3866"/><path d="M5 4l2.5 0 1 3-1.5 1c.7 1.5 1.5 2.3 3 3l1-1.5 3 1V14c-5 .5-9.5-4-9-10z" fill="#fff"/></svg>
        <span>205-555-0143</span>
      </li>
      <li>
        <svg class="icon" viewBox="0 0 18 18"><rect width="18" height="18" fill="#1d3866"/><path d="M9 3.5a3.5 3.5 0 0 1 3.5 3.5c0 2.5-3.5 7-3.5 7S5.5 9.5 5.5 7A3.5 3.5 0 0 1 9 3.5z" fill="#fff"/><circle cx="9" cy="7" r="1.3" fill="#1d3866"/></svg>
        <span>418 Wrenfield Crest Drive,<br>Suite 140 Birmingham, AL 35999</span>
      </li>
      <li>
        <svg class="icon" viewBox="0 0 18 18"><rect width="18" height="18" fill="#1d3866"/><circle cx="9" cy="9" r="5" fill="none" stroke="#fff" stroke-width="1.3"/><path d="M4 9h10M9 4c-2 2.5-2 7.5 0 10M9 4c2 2.5 2 7.5 0 10" fill="none" stroke="#fff" stroke-width="1"/></svg>
        <span>www.dlmfabworks.example</span>
      </li>
    </ul>

    <div class="rule"></div>
    <div class="band"></div>
  </section>

  <section class="card card-back">
    <div class="plant-photo" role="img" aria-label="Photograph of insulated steel pipework inside an industrial plant, in cool blue tones"></div>
    <div class="logo-strip"></div>
    <div class="wordmark">DL&amp;M</div>
  </section>
</body>
</html>
```